Famous Australian Web Brand (Zentrivo.com.au) Needs a New Website & Logo

Zentrivo.com.au is one of the leading domain name registration businesses in Australia and is looking for an overhaul of its website and brand.

Zentrivo.com.au current products/services include domain name registration, web hosting, web site creation and SSL certificates.

In this design contest on Quorvane, we would like designers to create a new logo and new website design for Zentrivo.com.au.

Here is what contest entrants will need to create:
- 1 new logo
- 1 new home page design
- 1 internal page (pricing page)

The winning designer will receive the main prize of $750. In addition to this, the winning designer will have the opportunity to work with Zentrivo for the build of the full website and may get ongoing design work from Zentrivo.

thank you all for your designs, we are after a web 2.0 look and feel, please dont use serif fonts, lets use modern and sleek ones, i will upload some samples of one we like shortly

header is to be in black with some texturing, white fonts and the call to action buttons are in green.

for the 6 free services, please use round edges for the images with the text under it, as i will upload shortly and we would like custome images, not stockimage types please

im uploading a sample of a background image for the header, which is black with texturing and also and image for the footer/middle of the page which has the correct shading of the grey for the middle section

please see file 8 for the look we are trying to get with our site and for font ideas

Reason: we have decided to extend the contest for another 3 days as a couple of designers have requested a bit more time

Target Market(s)

People that might need to buy a domain name or start a website: small business owners; entrepreneurs; bloggers; everyone from mum-and-dad website owners to tech savvy entrepreneurs. Geographically we will be targeting Australia but this should not influence the design.

Industry/Entity Type

Build

Requirements
Must have
• The logo should:
- Have the text "Zentrivo"
- Be positioned in the top left hand corner of the website
- Be either a wordmark, pictorial or abstract logo. That is, text-only logos are acceptable but we are also interested in receiving logos with a mark to the left that could somehow represents the business that we’re in

The homepage should:
- Feel modern, slick, web2.0
- Have a horizontal menu with 4 menu items: About Us | Contact Us | My Cart | Login
- Include the logo at the top
- Include the content from this Word Document
- Include the rough layout and style from this JPG template layout

The interior page should:
- Have the same look and feel as the home page
- Include the rough layout and style from this JPG attachment
- Include the content from this second Word Document
Nice to have
• - Grey, white and black primary colors
- Buttons that are green or lime green with a web2.0 call to action
- Full-width design (i.e. across the screen like Quorvane)
Should not have
• - Do not include overt Australian references. While we are an Australian business we do not want Australian flags, kangaroos or Barnaby Wollop in our logo or on our website.
- Do not use the current red color scheme in the design. We want to move away from this.

```html
<!DOCTYPE html>
<html lang="en">
<head>
<meta charset="utf-8">
<title>Zentrivo – Domain Names</title>
<link href="https://fonts.googleapis.com/css2?family=Questrial&family=Arimo:wght@400;700&display=swap" rel="stylesheet">
<style>
:root{
  --black:#0b0b0b;
  --header:#262626;
  --green:#7cc52a;
  --green-dark:#4f9a14;
  --light:#ececec;
  --page:#f2f2f2;
  --text:#222;
  --muted:#8a8a8a;
  --rule:#555;
}
*{margin:0;padding:0;box-sizing:border-box}
html,body{width:960px;height:1200px;overflow:hidden}
body{position:relative;background:var(--page);font-family:"Arimo",Arial,sans-serif;color:var(--text)}
.abs{position:absolute}
.topbar{left:0;top:0;width:960px;height:28px;background:var(--black)}
.topbar ul{list-style:none;position:absolute;right:96px;top:0;display:flex;height:28px}
.topbar li{font-size:10px;color:#ddd;padding:0 12px;line-height:28px;border-left:1px solid #333}
.topbar li:first-child{border-left:none}
.header{left:0;top:28px;width:960px;height:241px;background:radial-gradient(ellipse at 50% 30%,#333 0%,var(--header) 55%,#1a1a1a 100%)}
.logo-mark{left:129px;top:31px;width:50px;height:50px;background:var(--green)}
.logo-name{left:186px;top:44px;font-family:"Questrial",sans-serif;font-size:22px;color:#fff;letter-spacing:1px}
.mainnav{left:493px;top:51px;display:flex;gap:0;font-family:"Questrial",sans-serif;font-size:12px;color:#ccc}
.mainnav span{position:absolute;white-space:nowrap;top:0}
.headline{left:120px;top:94px;font-family:"Questrial",sans-serif;font-size:32px;line-height:34px;color:#fff}
.ask{left:672px;top:113px;font-family:"Questrial",sans-serif;font-size:15px;color:var(--green);letter-spacing:.5px}
.ask-phone{left:672px;top:132px;font-family:"Questrial",sans-serif;font-size:25px;color:#fff}
.hrule{left:102px;top:170px;width:768px;height:1px;background:#444}
.searchbox{left:102px;top:186px;width:764px;height:48px;background:#111;border-radius:4px;border:1px solid #3a3a3a}
.search-input{left:110px;top:194px;width:553px;height:31px;background:#fff;border:1px solid #bbb;font-size:12px;font-weight:700;padding:10px 13px;letter-spacing:1px}
.tld{left:663px;top:194px;width:65px;height:31px;background:linear-gradient(#fff,#ddd);border:1px solid #bbb;font-size:11px;font-weight:700;padding:9px 0 0 8px}
.search-btn{left:746px;top:194px;width:108px;height:31px;border-radius:3px;background:linear-gradient(#9ad94a,var(--green-dark));color:#fff;font-family:"Questrial",sans-serif;font-size:13px;letter-spacing:1px;text-align:center;line-height:31px}
.sublinks span{position:absolute;top:244px;font-size:12px;color:#eee;letter-spacing:1px;white-space:nowrap}
.videoband{left:0;top:269px;width:960px;height:113px;background:var(--light);border-top:2px solid #fff}
.video{width:184px;height:87px;top:285px;background:#fff;border:1px solid #ccc}
.video .photo{position:absolute;right:0;top:0;width:110px;height:69px;background:linear-gradient(135deg,#fff,#d7c2b4)}
.video .play{position:absolute;left:38px;top:20px}
.video .cap{position:absolute;left:0;bottom:0;width:100%;height:18px;background:#111;color:#fff;font-size:9px;font-weight:700;text-align:center;line-height:18px}
.tagline{left:206px;top:394px;width:538px;height:59px;background:#fff;border:1px solid #ccc;font-family:"Questrial",sans-serif;font-size:20px;line-height:24px;text-align:center;padding-top:6px;color:#222}
.tagline b{font-weight:400;color:#000}
.feat-img{width:214px;height:158px;border-radius:5px;border:1px solid #ccc}
.social{background:linear-gradient(135deg,#6a2f63,#2b4e8b 45%,#3a7f3b 80%,#c98a2a)}
.mailart{background:radial-gradient(circle at 55% 45%,#9fd0f4,#2e86d2 50%,#114f96)}
.blogart{background:linear-gradient(90deg,#fff 58%,#111 58%)}
.photos{background:linear-gradient(135deg,#2a2a2a,#8a7f74 50%,#1b1b1b)}
.feat-title{font-family:"Questrial",sans-serif;font-size:13.5px;color:#111;white-space:nowrap}
.feat-desc{width:232px;height:48px;overflow:hidden;font-size:10px;line-height:16px;color:var(--muted)}
.footer{left:0;top:1038px;width:960px;height:162px;background:var(--black)}
.fcol{top:1064px;width:98px}
.fcol h4{font-family:"Questrial",sans-serif;font-weight:400;font-size:11px;color:#999;padding-bottom:4px;border-bottom:1px solid #444;letter-spacing:.5px}
.fcol li{list-style:none;font-size:8.5px;color:#ccc;line-height:17px;border-bottom:1px solid #333}
.fq{left:684px;top:1066px;font-family:"Questrial",sans-serif;font-size:12.5px;color:#ddd;letter-spacing:.5px}
.fcontact{left:688px;top:1080px;font-family:"Questrial",sans-serif;font-size:22px;color:#fff;letter-spacing:4px}
.fphone{left:686px;top:1102px;font-family:"Questrial",sans-serif;font-size:25px;color:var(--green)}
</style>
</head>
<body>
<div class="abs topbar"><ul><li>About Us</li><li>Contact Us</li><li>My Cart</li><li>Login</li></ul></div>

<header class="abs header"></header>
<div class="abs logo-mark"></div>
<div class="abs logo-name">Zentrivo</div>
<nav class="abs mainnav">
  <span style="left:0;color:var(--green)">DOMAINS</span>
  <span style="left:81px">CREATOR</span>
  <span style="left:162px">EMAIL</span>
  <span style="left:223px">HOSTING</span>
  <span style="left:301px">MARKETING</span>
</nav>
<h1 class="abs headline" style="font-weight:400">You get a lot more<br>than just a domain name.</h1>
<div class="abs ask">HAVE A QUESTION?</div>
<div class="abs ask-phone">1300 44 72 19</div>
<div class="abs hrule"></div>
<div class="abs searchbox"></div>
<div class="abs search-input">www.</div>
<div class="abs tld">.COM
  <svg width="10" height="8" viewBox="0 0 10 8" style="position:absolute;right:8px;top:12px"><path d="M1 1l4 5 4-5" stroke="#333" stroke-width="2" fill="none"/></svg>
</div>
<div class="abs search-btn">SEARCH</div>
<div class="sublinks">
  <span style="left:110px">Renew a domain</span>
  <span style="left:253px">Transfer a domain</span>
  <span style="left:406px">View Price List</span>
</div>

<div class="abs videoband"></div>
<div class="abs video" style="left:154px">
  <div class="photo" role="img" aria-label="Smiling businesswoman portrait"></div>
  <svg class="play" width="26" height="26" viewBox="0 0 26 26"><circle cx="13" cy="13" r="12" fill="#eee" stroke="#ccc"/><circle cx="13" cy="13" r="9" fill="#6cc02a"/><path d="M10 8l8 5-8 5z" fill="#fff"/></svg>
  <div class="cap">Everyone needs a domain name</div>
</div>
<div class="abs video" style="left:384px">
  <div class="photo" role="img" aria-label="Smiling young woman portrait"></div>
  <svg class="play" width="26" height="26" viewBox="0 0 26 26"><circle cx="13" cy="13" r="12" fill="#eee" stroke="#ccc"/><circle cx="13" cy="13" r="9" fill="#6cc02a"/><path d="M10 8l8 5-8 5z" fill="#fff"/></svg>
  <div class="cap">How you can use a domain name</div>
</div>
<div class="abs video" style="left:614px">
  <div class="photo" role="img" aria-label="Woman giving thumbs up"></div>
  <svg class="play" width="26" height="26" viewBox="0 0 26 26"><circle cx="13" cy="13" r="12" fill="#eee" stroke="#ccc"/><circle cx="13" cy="13" r="9" fill="#6cc02a"/><path d="M10 8l8 5-8 5z" fill="#fff"/></svg>
  <div class="cap">Why choose Zentrivo</div>
</div>

<div class="abs tagline">Everything your business needs to be successful<br>online is <b>FREE</b> with every domain name.</div>

<div class="abs feat-img social" style="left:119px;top:478px" role="img" aria-label="Colourful grid of social app tiles with the word Social"></div>
<div class="abs feat-title" style="left:121px;top:649px">Free 15 Page Website</div>
<p class="abs feat-desc" style="left:120px;top:670px">Create a professional, full-featured website in minutes without any technical knowledge. Choose from 4,000+ stunning website designs and</p>

<div class="abs feat-img mailart" style="left:382px;top:476px" role="img" aria-label="Envelopes swirling across a blue background"></div>
<div class="abs feat-title" style="left:380px;top:649px">Free Professional Email</div>
<p class="abs feat-desc" style="left:381px;top:670px">Having a personalised address that matches your domain name (for example, Tom@TomsPretzels.com or Sales@TomsPretzels.com) gives your company a</p>

<div class="abs feat-img blogart" style="left:655px;top:478px" role="img" aria-label="Blogging platform list beside a dark panel"></div>
<div class="abs feat-title" style="left:656px;top:649px">Free Website Hosting</div>
<p class="abs feat-desc" style="left:656px;top:670px">We provide the fast and secure hosting for your website. We take care of all the maintenance so all you have to do is create content for your site. Best</p>

<div class="abs feat-img social" style="left:117px;top:752px" role="img" aria-label="Colourful grid of social app tiles with the word Social"></div>
<div class="abs feat-title" style="left:116px;top:926px">Free Search Engine Optimisation</div>
<p class="abs feat-desc" style="left:118px;top:951px">What good is the best looking website if no one visits it? We thought about that too! All our sites are optimised for search engines by default to</p>

<div class="abs feat-img photos" style="left:381px;top:750px" role="img" aria-label="Grid of fashion portrait photographs"></div>
<div class="abs feat-title" style="left:382px;top:926px">Free Business Class Support</div>
<p class="abs feat-desc" style="left:381px;top:952px">This is a point of pride for us and we are here to help. We're available to you 24 hours a day, everyday. Many of our competitors don't even</p>

<div class="abs feat-img blogart" style="left:653px;top:752px" role="img" aria-label="Blogging platform list beside a dark panel"></div>
<div class="abs feat-title" style="left:648px;top:926px">Guaranteed renewal price</div>
<p class="abs feat-desc" style="left:650px;top:952px">You'll never pay more to renew your domain name than the rate you paid when you initially registered it, or what our registration rate was when you</p>

<footer class="abs footer"></footer>
<div class="abs fcol" style="left:118px"><h4>DOMAINS</h4><ul><li>Register Domains</li><li>Transfer Domains</li><li>Renew Domains</li><li>Name Servers</li></ul></div>
<div class="abs fcol" style="left:238px"><h4>CREATOR</h4><ul><li>Menu Item</li><li>Menu Item</li><li>Menu Item</li><li>Menu Item</li></ul></div>
<div class="abs fcol" style="left:357px;width:76px"><h4>EMAIL</h4><ul><li>Menu Item</li><li>Menu Item</li><li>Menu Item</li><li>Menu Item</li></ul></div>
<div class="abs fcol" style="left:453px"><h4>HOSTING</h4><ul><li>Menu Item</li><li>Menu Item</li><li>Menu Item</li><li>Menu Item</li></ul></div>
<div class="abs fcol" style="left:571px;width:72px"><h4>MARKETING</h4><ul><li>Menu Item</li><li>Menu Item</li><li>Menu Item</li><li>Menu Item</li></ul></div>
<div class="abs fq">HAVE A QUESTION FOR US?</div>
<div class="abs fcontact">CONTACT US</div>
<div class="abs fphone">1300 44 72 19</div>
</body>
</html>
```